A clean crisp business card for a Landscape Construction company. Designed to be easy to read contact/ info and also be appealing/interesting, unlike a traditional business card.

Industry/Entity Type

Landscape Construction

Contact Information for Business Card

Company name : Bramblecrest Landscape Construction, phone number: (877) 62Vales, website:Bramblecrestlandscapes.example, Email, sales@bramblecrestlandscapes.example

Requirements
Nice to have
• Luxurious finishes/ details…. Icons or emblems next to contact info
Should not have
• Clipart or general pictures

```html
<!DOCTYPE html>
<html lang="en">
<head>
<meta charset="utf-8">
<title>Bramblecrest Landscape Construction – Business Card</title>
<link rel="stylesheet" href="https://fonts.googleapis.com/css2?family=Libre+Bodoni:wght@400;700&display=swap">
<style>
  :root {
    --page: #ebebeb;
    --card-white: #f1f1f1;
    --brand-blue: #00438b;
    --icon-blue: #1f5fa6;
    --brand-green: #8cba32;
    --ink: #1a1a1a;
    --paper-text: #f4f4f4;
  }
  * { margin: 0; padding: 0; box-sizing: border-box; }
  html, body {
    width: 1200px; height: 800px; overflow: hidden;
    background: var(--page);
    font-family: "Libre Bodoni", Georgia, serif;
  }
  .canvas { position: relative; width: 1200px; height: 800px; }

  .card {
    position: absolute;
    width: 422px; height: 235px;
    overflow: hidden;
  }

  /* Front */
  .card-front {
    left: 287px; top: 115px;
    background: var(--brand-blue);
    color: var(--paper-text);
  }
  .front-brand {
    position: absolute; left: 0; right: 0; top: 126px;
    text-align: center;
  }
  .front-name {
    font-size: 27px; font-weight: 400;
    letter-spacing: 1px; text-transform: uppercase;
    line-height: 1;
  }
  .front-tagline {
    margin-top: 7px;
    font-size: 10.5px; font-weight: 400;
    letter-spacing: 3.6px; text-transform: uppercase;
  }

  /* Back */
  .card-back {
    left: 498px; top: 438px;
    background: var(--card-white);
    color: var(--ink);
  }
  .back-brand {
    position: absolute; left: 28px; top: 62px;
    font-size: 18px; font-weight: 400;
    color: var(--brand-blue);
    letter-spacing: 0.5px;
    line-height: 1;
  }
  .company-heading {
    position: absolute; left: 28px; top: 108px;
    font-size: 13.5px; font-weight: 700;
    line-height: 17px; text-transform: uppercase;
  }
  .contact-list {
    position: absolute; left: 28px; top: 152px;
    list-style: none;
  }
  .contact-item {
    display: flex; align-items: center;
    height: 23px;
    font-size: 11px;
    letter-spacing: 0.3px;
  }
  .contact-icon {
    width: 17px; height: 17px; margin-right: 6px;
    flex: none;
  }
  .accent-panel {
    position: absolute; right: -150px; top: -10px;
    width: 255px; height: 255px;
    border-radius: 50%;
    background: radial-gradient(circle at 60% 50%, var(--icon-blue) 0%, #5f9a5a 45%, var(--brand-green) 75%, var(--brand-green) 100%);
  }
</style>
</head>
<body>
<main class="canvas">

  <section class="card card-front" aria-label="Card front">
    <div class="front-brand">
      <p class="front-name">Bramblecrest</p>
      <p class="front-tagline">Landscape Construction</p>
    </div>
  </section>

  <section class="card card-back" aria-label="Card back">
    <p class="back-brand">Bramblecrest</p>

    <h1 class="company-heading">Bramblecrest<br>Landscape Construction</h1>

    <ul class="contact-list">
      <li class="contact-item">
        <svg class="contact-icon" viewBox="0 0 20 20" aria-hidden="true">
          <circle cx="10" cy="10" r="10" fill="var(--icon-blue)"/>
          <path d="M7 5.5l1.6 0 .8 2.3-1.1.8a6 6 0 0 0 3.1 3.1l.8-1.1 2.3.8v1.6c0 .6-.5 1-1.1 1A8.6 8.6 0 0 1 6 6.6c0-.6.4-1.1 1-1.1z" fill="#fff"/>
        </svg>
        (877) 62Vales
      </li>
      <li class="contact-item">
        <svg class="contact-icon" viewBox="0 0 20 20" aria-hidden="true">
          <circle cx="10" cy="10" r="10" fill="var(--icon-blue)"/>
          <g fill="none" stroke="#fff" stroke-width="0.9">
            <circle cx="10" cy="10" r="5.5"/>
            <ellipse cx="10" cy="10" rx="2.4" ry="5.5"/>
            <path d="M4.5 10h11M5.3 7.2h9.4M5.3 12.8h9.4"/>
          </g>
        </svg>
        Bramblecrestlandscapes.example
      </li>
      <li class="contact-item">
        <svg class="contact-icon" viewBox="0 0 20 20" aria-hidden="true">
          <circle cx="10" cy="10" r="10" fill="var(--icon-blue)"/>
          <g fill="none" stroke="#fff" stroke-width="0.9">
            <rect x="5" y="6.5" width="10" height="7.5"/>
            <path d="M5 6.5l5 4 5-4M5 14l3.6-3.3M15 14l-3.6-3.3"/>
          </g>
        </svg>
        sales@bramblecrestlandscapes.example
      </li>
    </ul>

    <div class="accent-panel" role="img" aria-label="Large green-to-blue brand emblem decoration at the card edge"></div>
  </section>

</main>
</body>
</html>
```